IT-support company web-site design

We need to re-design out site for existing clients and for the future promotions. Site needs to be attractive with intuitive interface. We need to keep our logo and colors but any reshuffles can be made. I provide the working site and re-made version, which we do nt like. It has to be more bright and clear. All the blocks have to be divided and look like logic and structured. PLease find the addresses to work with below.
The "real" one https://qorbil.com
The version http://tomuski.net/Qorbil/
If you have any с

Industry/Entity Type

It Company

Number of Pages Required

5+ page

Font styles to use
Sans Serif

Colors
9bcb3c

Requirements
Must have
• Our LOGO and our colors (green palette). We d like to make our services blocks as the main things. We need to have our images and slogans as there are extremely important advantages of our company.
Nice to have
• Original and modern view of the site.
Should not have
• unpredictable and @surprising@, hard- definable buttons and ways

```html
<!DOCTYPE html>
<html lang="en">
<head>
<meta charset="utf-8">
<title>Qorbil – IT Support</title>
<link href="https://fonts.googleapis.com/css2?family=Lato:wght@400;700;900&family=Open+Sans:wght@400;600;700&display=swap" rel="stylesheet">
<style>
:root{
  --green:#9bcb3c;
  --green-dark:#7fb42a;
  --ink:#2b2b2b;
  --text:#555;
  --muted:#888;
  --line:#e4e4e4;
  --footer:#2f2f2f;
  --footer-text:#cfcfcf;
  --light-bg:#f3f3f3;
}
*{box-sizing:border-box;margin:0;padding:0}
html,body{width:1200px;height:3114px;overflow:hidden}
body{position:relative;background:#fff;font-family:"Open Sans",Arial,sans-serif;color:var(--text)}
.abs{position:absolute}
a{color:inherit;text-decoration:none}

/* header */
.site-header{left:0;top:0;width:1200px;height:128px;background:#fff;border-top:4px solid var(--green)}
.brand{left:100px;top:42px;display:flex;align-items:center;gap:12px;font-family:"Lato",sans-serif;font-weight:400;font-size:38px;letter-spacing:2px;color:#555}
.brand .dot{width:34px;height:34px;border-radius:50%;border:3px solid var(--green)}
.header-phone{left:735px;top:34px;font-family:"Lato",sans-serif;font-size:17px;color:#555;display:flex;align-items:center;gap:8px}
.login-btn{left:930px;top:30px;width:170px;height:34px;border-radius:17px;background:var(--green);color:#fff;font-family:"Lato",sans-serif;font-weight:700;font-size:12.5px;display:flex;align-items:center;justify-content:center;gap:6px}
.main-nav{left:440px;top:84px;width:662px;display:flex;justify-content:space-between;font-family:"Lato",sans-serif;font-weight:700;font-size:14.5px;color:#333}

/* hero */
.hero{left:0;top:128px;width:1200px;height:650px;overflow:hidden;background:linear-gradient(135deg,#cfd6db 0%,#a9b3bb 35%,#e7eaec 60%,#8e9aa4 100%)}
.hero-title{left:0;top:462px;width:1200px;text-align:center;font-family:"Lato",sans-serif;font-weight:900;font-size:58px;line-height:80px;color:#fff;text-shadow:0 2px 6px rgba(0,0,0,.35)}
.hero-arrow{top:440px;color:#fff;font-size:22px}

/* section heads */
.section-title{left:0;width:1200px;text-align:center;font-family:"Lato",sans-serif;font-weight:700;font-size:34px;color:var(--ink);letter-spacing:.5px}
.section-title span{color:var(--green)}
.title-rule{left:530px;width:140px;height:14px}
.section-lead{text-align:center;font-size:12.5px;line-height:26px;color:var(--muted)}

/* service cards */
.service-card{width:312px;height:216px;border:1px solid var(--line);background:#fff;text-align:center}
.service-badge{width:150px;height:70px}
.service-card h3{margin-top:50px;font-family:"Lato",sans-serif;font-weight:700;font-size:17px;color:var(--ink)}
.service-card p{margin:14px auto 0;width:270px;font-size:12.3px;line-height:25px;color:var(--muted)}
.read-more{display:inline-flex;align-items:center;gap:6px;margin-top:12px;font-family:"Lato",sans-serif;font-weight:700;font-size:13px;color:var(--green)}

/* benefits band */
.benefits{left:0;top:1395px;width:1200px;height:312px;background:linear-gradient(90deg,#9bcb3c 0%,#a8d257 45%,#93c53a 100%)}
.benefit{width:220px;text-align:center;color:#fff;font-family:"Lato",sans-serif;font-weight:700;font-size:15.5px;line-height:25px}
.benefit svg{display:block;margin:0 auto 14px}

/* about */
.about-title{left:100px;top:1780px;font-family:"Lato",sans-serif;font-weight:700;font-size:34px;color:var(--ink)}
.about-title span{color:var(--green)}
.about-text{left:100px;width:460px;font-size:13.3px;line-height:26px;color:#444}
.pill-btn{border-radius:22px;background:var(--green);color:#fff;font-family:"Lato",sans-serif;font-weight:700;font-size:13px;display:flex;align-items:center;justify-content:center;gap:6px}
.video-frame{left:612px;top:1794px;width:486px;height:283px;border:4px solid #fff;box-shadow:0 0 0 1px var(--line);background:linear-gradient(120deg,#d9d3cb 0%,#b7aa9c 40%,#e9e5e0 70%,#8d8f95 100%)}
.play{left:220px;top:118px;width:48px;height:48px;border-radius:50%;background:#e52d27}

/* partners */
.partners{left:0;top:2160px;width:1200px;height:440px;background:linear-gradient(160deg,#f7f7f7,#ececec)}
.partner-tile{top:2373px;width:185px;height:108px;background:#fff;border:1px solid #dcdcdc;display:flex;align-items:center;justify-content:center}
.partner-tile i{display:block;width:120px;height:36px;border-radius:4px;background:#d7dde3}

/* footer */
.footer-wave{left:0;top:2540px;width:1200px;height:120px}
.site-footer{left:0;top:2640px;width:1200px;height:474px;background:var(--footer)}
.footer-brand{left:0;top:2648px;width:1200px;display:flex;justify-content:center;align-items:center;gap:12px;font-family:"Lato",sans-serif;font-weight:400;font-size:46px;letter-spacing:3px;color:#fff}
.footer-brand .dot{width:38px;height:38px;border-radius:50%;border:3px solid #fff}
.footer-col h4{font-family:"Lato",sans-serif;font-weight:700;font-size:16.5px;color:#fff;letter-spacing:.5px;margin-bottom:22px}
.footer-col li{list-style:none;font-size:12.5px;color:var(--footer-text);height:31px;display:flex;align-items:center;gap:10px}
.footer-col li b{color:#fff;font-weight:400;font-size:11px}
.contact-list li{align-items:flex-start;height:auto;margin-bottom:16px;line-height:22px}
.newsletter p{font-size:12.3px;line-height:22px;color:var(--footer-text);width:300px}
.email-field{margin-top:16px;width:256px;height:42px;border:1px solid #bbb;color:#fff;font-size:12px;display:flex;align-items:center;padding-left:12px}
.footer-rule{left:100px;top:3022px;width:1000px;height:1px;background:#555}
.copyright{left:100px;top:3061px;font-size:12px;color:var(--footer-text)}
.social{top:3052px;width:38px;height:38px;border-radius:50%;border:2px solid #ddd}
</style>
</head>
<body>

<header class="abs site-header">
  <div class="abs brand" style="top:38px"><span class="dot"></span>QORBIL</div>
  <div class="abs header-phone">
    <svg width="16" height="16" viewBox="0 0 24 24"><path fill="#9bcb3c" d="M6.6 10.8a15.1 15.1 0 0 0 6.6 6.6l2.2-2.2a1 1 0 0 1 1-.25 11.4 11.4 0 0 0 3.6.57 1 1 0 0 1 1 1V20a1 1 0 0 1-1 1A17 17 0 0 1 3 4a1 1 0 0 1 1-1h3.5a1 1 0 0 1 1 1c0 1.25.2 2.45.57 3.57a1 1 0 0 1-.25 1z"/></svg>
    (415) - 380 - 2716
  </div>
  <a class="abs login-btn" href="#">
    <svg width="11" height="12" viewBox="0 0 12 14"><rect x="1" y="6" width="10" height="8" rx="1" fill="#fff"/><path d="M3 6V4a3 3 0 0 1 6 0v2" stroke="#fff" stroke-width="1.6" fill="none"/></svg>
    CUSTOMERS LOGIN
  </a>
  <nav class="abs main-nav">
    <a href="#">QORBIL DIFFERENCE</a><a href="#">SERVICES</a><a href="#">CUSTOMERS</a><a href="#">RESOURCES</a><a href="#">SUPPORT</a><a href="#">MORE ▾</a>
  </nav>
</header>

<section class="abs hero" role="img" aria-label="Help desk team with headsets working at computers in a bright office">
</section>
<svg class="abs" style="left:0;top:640px" width="1200" height="140" viewBox="0 0 1200 140">
  <path d="M0 36 Q600 190 1200 60 L1200 140 L0 140 Z" fill="#fff"/>
  <path d="M0 36 Q600 190 1200 60" stroke="#9bcb3c" stroke-width="5" fill="none"/>
</svg>
<h1 class="abs hero-title">WE MAKE IT SIMPLE<br>AND SECURE</h1>
<div class="abs hero-arrow" style="left:36px">‹</div>
<div class="abs hero-arrow" style="left:1150px">›</div>

<!-- services -->
<h2 class="abs section-title" style="top:852px"><span>OUR</span> SERVICES</h2>
<svg class="abs title-rule" style="top:904px" viewBox="0 0 140 14"><line x1="0" y1="7" x2="56" y2="7" stroke="#ccc"/><line x1="84" y1="7" x2="140" y2="7" stroke="#ccc"/><circle cx="70" cy="7" r="5" fill="none" stroke="#9bcb3c" stroke-width="1.5"/></svg>
<p class="abs section-lead" style="left:285px;top:938px;width:630px">Lorem Ipsum is simply dummy text of the printing and typesetting industry. Lorem Ipsum has been the industry's standard dummy text ever since the 1500s, when an unknown printer took a galley of type book.</p>

<div class="abs service-card" style="left:98px;top:1094px">
  <h3>SOFTWARE SERVICES</h3>
  <p>Lorem Ipsum is simply dummy text of the printing and typesetting industry. Lorem Ipsum has been the industry's standard</p>
  <a class="read-more" href="#">READ MORE <svg width="13" height="13" viewBox="0 0 14 14"><circle cx="7" cy="7" r="7" fill="#9bcb3c"/><path d="M6 4l3 3-3 3" stroke="#fff" stroke-width="1.8" fill="none"/></svg></a>
</div>
<div class="abs service-card" style="left:444px;top:1094px">
  <h3>CUSTOMER SERVICES</h3>
  <p>Lorem Ipsum is simply dummy text of the printing and typesetting industry. Lorem Ipsum has been the industry's standard</p>
  <a class="read-more" href="#">READ MORE <svg width="13" height="13" viewBox="0 0 14 14"><circle cx="7" cy="7" r="7" fill="#9bcb3c"/><path d="M6 4l3 3-3 3" stroke="#fff" stroke-width="1.8" fill="none"/></svg></a>
</div>
<div class="abs service-card" style="left:789px;top:1094px">
  <h3>BUSINESS SERVICES</h3>
  <p>Lorem Ipsum is simply dummy text of the printing and typesetting industry. Lorem Ipsum has been the industry's standard</p>
  <a class="read-more" href="#">READ MORE <svg width="13" height="13" viewBox="0 0 14 14"><circle cx="7" cy="7" r="7" fill="#9bcb3c"/><path d="M6 4l3 3-3 3" stroke="#fff" stroke-width="1.8" fill="none"/></svg></a>
</div>

<!-- badges above cards -->
<svg class="abs service-badge" style="left:179px;top:1030px" viewBox="0 0 150 70"><path d="M2 66 C2 40 22 34 36 38 C40 10 70 2 84 14 C100 4 126 14 126 36 C142 36 148 52 148 66" fill="#fff" stroke="#9bcb3c" stroke-width="2.5"/><rect x="62" y="30" width="26" height="17" rx="2" fill="#333"/><rect x="71" y="47" width="8" height="5" fill="#333"/><rect x="50" y="55" width="12" height="9" fill="#333"/><rect x="88" y="55" width="12" height="9" fill="#333"/><path d="M56 55v-3h38v3" stroke="#333" stroke-width="2" fill="none"/></svg>
<svg class="abs service-badge" style="left:525px;top:1030px" viewBox="0 0 150 70"><path d="M2 66 C2 40 22 34 36 38 C40 10 70 2 84 14 C100 4 126 14 126 36 C142 36 148 52 148 66" fill="#fff" stroke="#9bcb3c" stroke-width="2.5"/><circle cx="75" cy="34" r="9" fill="#333"/><path d="M58 64c0-12 8-18 17-18s17 6 17 18z" fill="#333"/><path d="M64 34a11 11 0 0 1 22 0" stroke="#333" stroke-width="2.5" fill="none"/></svg>
<svg class="abs service-badge" style="left:870px;top:1030px" viewBox="0 0 150 70"><path d="M2 66 C2 40 22 34 36 38 C40 10 70 2 84 14 C100 4 126 14 126 36 C142 36 148 52 148 66" fill="#fff" stroke="#9bcb3c" stroke-width="2.5"/><rect x="57" y="34" width="36" height="28" rx="3" fill="#333"/><rect x="67" y="27" width="16" height="8" rx="2" fill="none" stroke="#333" stroke-width="3"/><rect x="57" y="44" width="36" height="3" fill="#fff"/></svg>

<!-- benefits band -->
<section class="abs benefits" aria-label="Advantages">
  <div class="abs benefit" style="left:52px;top:80px">
    <svg width="96" height="100" viewBox="0 0 96 100"><ellipse cx="38" cy="18" rx="30" ry="10" fill="#fff"/><path d="M8 26c0 6 13 10 30 10s30-4 30-10v14c0 6-13 10-30 10S8 46 8 40z" fill="#fff"/><path d="M8 48c0 6 13 10 30 10s30-4 30-10v14c0 6-13 10-30 10S8 68 8 62z" fill="#fff"/><circle cx="72" cy="74" r="14" fill="none" stroke="#fff" stroke-width="7" stroke-dasharray="5 3"/><circle cx="72" cy="74" r="5" fill="#fff"/></svg>
    FREEDOM FROM<br>IT WORRIES
  </div>
  <div class="abs benefit" style="left:266px;top:80px">
    <svg width="130" height="100" viewBox="0 0 130 100"><path d="M20 86a18 18 0 0 1 4-36 28 28 0 0 1 52-14 22 22 0 0 1 34 20 15 15 0 0 1-2 30z" fill="#fff"/><rect x="52" y="50" width="26" height="22" rx="2" fill="#9bcb3c"/><path d="M57 50v-6a8 8 0 0 1 16 0v6" stroke="#9bcb3c" stroke-width="4" fill="none"/></svg>
    WORK SECURELY FROM<br>ANYWHERE
  </div>
  <div class="abs benefit" style="left:478px;top:80px">
    <svg width="96" height="100" viewBox="0 0 96 100"><circle cx="42" cy="30" r="16" fill="#fff"/><path d="M22 30a20 20 0 0 1 40 0" stroke="#fff" stroke-width="4" fill="none"/><path d="M14 92c0-22 12-34 28-34s28 12 28 34z" fill="#fff"/><circle cx="70" cy="78" r="15" fill="#fff"/><text x="70" y="85" text-anchor="middle" font-family="Lato,sans-serif" font-weight="900" font-size="20" fill="#9bcb3c">?</text></svg>
    24/7 HELP DESK<br>SUPPORT
  </div>
  <div class="abs benefit" style="left:690px;top:80px">
    <svg width="130" height="100" viewBox="0 0 130 100"><path d="M20 86a18 18 0 0 1 4-36 28 28 0 0 1 52-14 22 22 0 0 1 34 20 15 15 0 0 1-2 30z" fill="#fff"/><path d="M54 48l20 20M74 48L54 68" stroke="#9bcb3c" stroke-width="8" stroke-linecap="round"/></svg>
    ELIMINATE UNPREDICTABLE<br>IT EXPENSES.
  </div>
  <div class="abs benefit" style="left:924px;top:80px">
    <svg width="96" height="100" viewBox="0 0 96 100"><circle cx="44" cy="46" r="32" fill="none" stroke="#fff" stroke-width="6"/><text x="44" y="60" text-anchor="middle" font-family="Lato,sans-serif" font-weight="900" font-size="40" fill="#fff">$</text><rect x="66" y="58" width="14" height="22" fill="#fff"/><path d="M58 78h30L73 96z" fill="#fff"/></svg>
    WE ARE REDUCE<br>IT COSTS
  </div>
</section>

<!-- about -->
<h2 class="abs about-title"><span>ABOUT</span> COMPANY</h2>
<p class="abs about-text" style="top:1852px">Lower your total IT costs with Qorbil's simple flat fee structure so you can focus on growing your business.</p>
<p class="abs about-text" style="top:1920px">Qorbil's secure IT systems delivered 100% uninterrupted service during all hurricanes and tropical storms since 2000 including Allison, Rita, Ike and Harvey. Qorbil provides live local 24/7 Help Desk and Tier 3 support</p>
<a class="abs pill-btn" style="left:100px;top:2036px;width:134px;height:40px" href="#">READ MORE <svg width="13" height="13" viewBox="0 0 14 14"><circle cx="7" cy="7" r="7" fill="#fff"/><path d="M6 4l3 3-3 3" stroke="#9bcb3c" stroke-width="1.8" fill="none"/></svg></a>
<div class="abs video-frame" role="img" aria-label="Video still of a smiling team member in an office with colleagues behind">
  <div class="abs play"><svg width="48" height="48" viewBox="0 0 48 48"><path d="M19 15l15 9-15 9z" fill="#fff"/></svg></div>
</div>

<!-- partners -->
<section class="abs partners"></section>
<h2 class="abs section-title" style="top:2224px"><span>OUR</span> PARTNERS</h2>
<svg class="abs title-rule" style="top:2276px" viewBox="0 0 140 14"><line x1="0" y1="7" x2="56" y2="7" stroke="#ccc"/><line x1="84" y1="7" x2="140" y2="7" stroke="#ccc"/><circle cx="70" cy="7" r="5" fill="none" stroke="#9bcb3c" stroke-width="1.5"/></svg>
<p class="abs section-lead" style="left:0;top:2312px;width:1200px">Companies worldwide trust Qorbil to help them maximize the value of IT and improve user efficiency and productivity.</p>
<div class="abs partner-tile" style="left:100px" aria-label="Partner"><i></i></div>
<div class="abs partner-tile" style="left:303px" aria-label="Partner"><i></i></div>
<div class="abs partner-tile" style="left:509px" aria-label="Partner"><i></i></div>
<div class="abs partner-tile" style="left:710px" aria-label="Partner"><i></i></div>
<div class="abs partner-tile" style="left:914px" aria-label="Partner"><i></i></div>

<!-- footer -->
<svg class="abs footer-wave" viewBox="0 0 1200 120" preserveAspectRatio="none">
  <path d="M0 100 Q150 30 300 60 Q600 -20 900 60 Q1050 30 1200 100 L1200 120 L0 120 Z" fill="#2f2f2f"/>
  <path d="M0 100 Q150 30 300 60 Q600 -20 900 60 Q1050 30 1200 100" stroke="#9bcb3c" stroke-width="5" fill="none"/>
</svg>
<footer class="abs site-footer"></footer>
<div class="abs footer-brand"><span class="dot"></span>QORBIL</div>

<div class="abs footer-col" style="left:100px;top:2778px">
  <h4>CONTACT US</h4>
  <ul class="contact-list">
    <li><svg width="14" height="18" viewBox="0 0 14 18"><path d="M7 1a6 6 0 0 1 6 6c0 4.5-6 10-6 10S1 11.5 1 7a6 6 0 0 1 6-6z" fill="none" stroke="#ccc" stroke-width="1.4"/><circle cx="7" cy="7" r="2" fill="#ccc"/></svg><span>Old Simple Street, Old City,<br>New State</span></li>
    <li><svg width="14" height="14" viewBox="0 0 24 24"><path fill="#ccc" d="M6.6 10.8a15.1 15.1 0 0 0 6.6 6.6l2.2-2.2a1 1 0 0 1 1-.25 11.4 11.4 0 0 0 3.6.57 1 1 0 0 1 1 1V20a1 1 0 0 1-1 1A17 17 0 0 1 3 4a1 1 0 0 1 1-1h3.5a1 1 0 0 1 1 1c0 1.25.2 2.45.57 3.57a1 1 0 0 1-.25 1z"/></svg><span>(877) 412-5390</span></li>
    <li><svg width="16" height="12" viewBox="0 0 16 12"><rect x="1" y="1" width="14" height="10" fill="none" stroke="#ccc" stroke-width="1.4"/><path d="M1 1l7 6 7-6" fill="none" stroke="#ccc" stroke-width="1.4"/></svg><span>hello@qorbilmail.com</span></li>
  </ul>
</div>
<div class="abs footer-col" style="left:376px;top:2778px">
  <h4>COMPANY</h4>
  <ul><li><b>›</b>Home</li><li><b>›</b>About Us</li><li><b>›</b>Qorbil Difference</li><li><b>›</b>Our Services</li></ul>
</div>
<div class="abs footer-col" style="left:573px;top:2778px">
  <h4>RESOURCES</h4>
  <ul><li><b>›</b>Contact us</li><li><b>›</b>Book A Callback</li><li><b>›</b>FAQs</li><li><b>›</b>Terms &amp; Conditions</li></ul>
</div>
<div class="abs footer-col newsletter" style="left:801px;top:2778px">
  <h4>JOIN OUR NEWSLETTER</h4>
  <p>Sign up for our newsletter to stay up-to-date with our Company Informations</p>
  <div class="email-field">Email Address</div>
  <a class="pill-btn" style="margin-top:18px;width:100px;height:40px" href="#">SUBMIT</a>
</div>

<div class="abs footer-rule"></div>
<div class="abs copyright">© Copyright 2017 Qorbil. All Rights Reserved</div>
<div class="abs social" style="left:912px" aria-label="Social link"></div>
<div class="abs social" style="left:960px" aria-label="Social link"></div>
<div class="abs social" style="left:1010px" aria-label="Social link"></div>
<div class="abs social" style="left:1060px" aria-label="Social link"></div>

</body>
</html>
```